Website design for recruitment solutions

We connect top talents to fast growing employers in Asia. We need to revamp our existing website (currently outdated) and also add more pages to make it more informative for talents and employers.
We need final design output to be for both desktop and mobile devices. The final design output must come with all specifications so it's easier for our dev team to implement. We have a detailed mockup but we expect the design to be significantly changed by the final output. We want the pages to look aesthetic, modern and professional.
Number of Pages Required
5+ page
Requirements
Must have
- - To have Pages design for desktop+mobile. Need to take into account intermediate resolutions like 1365px\1023px\767px\479px, especially if mobile/desktop design differs considerably. Design should be repeatable (between pages), suitable for block-layout.
Nice to have
- In terms of receiving files, we usually work with designers who can deliver files in Figma or Sketch with export to Figma. If in PSD format - please export to Zeplin or Avocode, otherwise will be difficult to open

```html
<!DOCTYPE html>
<html lang="en">
<head>
<meta charset="utf-8">
<title>Hirevale Recruitment</title>
<link href="https://fonts.googleapis.com/css2?family=Montserrat:wght@300;400;500&display=swap" rel="stylesheet">
<style>
:root{
  --red:#f3000f;
  --blue:#1c86cf;
  --blue-bright:#1e8ff0;
  --ink:#2f2f2f;
  --muted:#6b6b6b;
  --line:#d9d9d9;
  --footer:#3d3d3d;
  --footer-text:#e6e6e6;
  --soft:#f5f2f1;
  --white:#ffffff;
}
*{margin:0;padding:0;box-sizing:border-box}
html,body{width:1200px;height:2995px;overflow:hidden}
body{position:relative;background:var(--white);font-family:"Montserrat",Arial,sans-serif;color:var(--ink);font-weight:300}
.abs{position:absolute}
a{color:inherit;text-decoration:none}

/* header */
.header{position:absolute;left:0;top:0;width:1200px;height:71px;border-bottom:1px solid #e6e6e6;background:var(--white);z-index:5}
.brand{position:absolute;left:45px;top:14px}
.brand-name{font-size:30px;font-weight:400;color:var(--ink);line-height:32px;letter-spacing:.5px}
.brand-sub{font-size:8px;letter-spacing:5px;color:var(--ink);margin-top:1px}
.nav a{position:absolute;top:27px;font-size:14px;color:var(--muted)}
.nav a.active{color:var(--ink)}
.nav a.active::after{content:"";position:absolute;left:0;right:0;top:24px;height:2px;background:var(--red)}
.btn-login{position:absolute;left:941px;top:15px;width:96px;height:41px;border:1px solid var(--blue-bright);color:var(--blue-bright);font-size:14px;display:flex;align-items:center;justify-content:center;font-weight:400}
.btn-register{position:absolute;left:1049px;top:15px;width:97px;height:41px;background:var(--red);color:var(--white);font-size:14px;display:flex;align-items:center;justify-content:center;font-weight:400}

/* hero */
.hero-title{left:47px;top:230px;font-size:36px;line-height:44px;font-weight:300;color:var(--ink)}
.hero-text{left:47px;top:337px;font-size:13.5px;line-height:18px;color:#444;width:380px}
.btn-red{position:absolute;background:var(--red);color:var(--white);font-size:15px;font-weight:400;display:flex;align-items:center;justify-content:center;gap:12px}
.scroll-btn{left:37px;top:638px;width:30px;height:30px;border-radius:50%;background:var(--white);box-shadow:0 1px 4px rgba(0,0,0,.2);display:flex;align-items:center;justify-content:center}
.photo{position:absolute;border-radius:50%}
.orbit{position:absolute;left:0;top:0}

/* profile cards */
.card{position:absolute;background:var(--white);box-shadow:0 1px 5px rgba(0,0,0,.16)}
.p-card{top:788px;width:204px;height:314px;padding:0 0 0 19px}
.p-card .avatar{position:absolute;left:60px;top:22px;width:84px;height:84px;border-radius:50%}
.p-name{position:absolute;top:125px;font-size:15px;font-weight:500;color:var(--ink)}
.p-role{position:absolute;top:152px;font-size:11.5px;line-height:15px;color:var(--muted);width:180px}
.p-list{position:absolute;top:198px;left:19px;right:12px;list-style:none}
.p-list li{font-size:10.5px;color:var(--muted);height:20.5px;display:flex;justify-content:space-between;align-items:center}
.tick{width:13px;height:13px;border-radius:50%;border:1px solid #cfe2f2;position:relative;flex:none}
.tick::after{content:"";position:absolute;left:4px;top:1.5px;width:3px;height:6px;border:solid var(--blue-bright);border-width:0 1.2px 1.2px 0;transform:rotate(40deg)}
.match-bar{position:absolute;background:var(--blue-bright);color:var(--white);font-size:14px;font-weight:400;display:flex;align-items:center;justify-content:space-between;padding:0 4px 0 18px}
.round-ico{width:28px;height:28px;border-radius:50%;border:1.5px solid var(--white);display:flex;align-items:center;justify-content:center;background:var(--white)}
.section-title{position:absolute;font-size:28px;font-weight:300;color:var(--ink)}
.section-text{position:absolute;font-size:13.5px;line-height:18px;color:#444}

/* insights */
.insights{left:0;top:1304px;width:600px;height:494px;background:var(--blue)}
.insights-photo{left:600px;top:1304px;width:600px;height:494px;background:linear-gradient(110deg,#8b7a6d 0%,#c9c4bd 35%,#e9ebea 60%,#d3d7d9 85%,#b9c1c6 100%)}
.btn-outline-white{position:absolute;left:89px;top:1599px;width:159px;height:49px;background:var(--white);color:var(--blue);font-size:15px;font-weight:400;display:flex;align-items:center;justify-content:center;gap:12px}
.mini-name{font-size:13px;font-weight:400;color:var(--ink)}
.mini-role{font-size:10.5px;color:var(--muted)}
.mini-list{position:absolute;list-style:none}
.mini-list li{font-size:9px;color:var(--muted);height:20.5px;display:flex;justify-content:space-between;align-items:center}
.dot{position:absolute;width:9px;height:9px;border-radius:50%;border:1px solid var(--white)}

/* people */
.t-card{top:2048px;width:252px;height:380px}
.t-card .avatar{position:absolute;left:74px;top:24px;width:104px;height:104px;border-radius:50%}
.t-name{position:absolute;left:22px;top:156px;font-size:15px;font-weight:500}
.t-role{position:absolute;left:22px;top:184px;font-size:11.5px;color:var(--muted)}
.t-quote{position:absolute;left:22px;top:215px;width:210px;font-size:11.3px;line-height:15px;color:var(--muted)}
.stars{position:absolute;left:22px;top:330px;display:flex;gap:8px}
.pager{position:absolute;width:11px;height:11px;border-radius:50%;border:1.5px solid var(--ink)}
.pager.on{background:var(--ink)}

/* footer */
.footer{left:0;top:2601px;width:1200px;height:394px;background:var(--footer);color:var(--footer-text)}
.f-head{position:absolute;top:62px;font-size:17px;font-weight:300;padding-bottom:14px;border-bottom:1px solid #555}
.f-text{position:absolute;left:44px;top:116px;width:320px;font-size:13px;line-height:17.5px}
.f-link{position:absolute;font-size:16px;font-weight:300}
.f-reg{position:absolute;left:491px;top:192px;width:106px;height:39px;border-radius:20px;background:var(--red);color:var(--white);font-size:15px;font-weight:400;display:flex;align-items:center;justify-content:center}
.social{position:absolute;top:251px;width:22px;height:22px;background:var(--footer-text)}
.f-rule{position:absolute;left:0;top:312px;width:1200px;height:1px;background:#555}
.f-small{position:absolute;top:335px;font-size:11.5px}
</style>
</head>
<body>

<svg width="0" height="0" style="position:absolute">
  <defs>
    <symbol id="star" viewBox="0 0 24 24"><polygon points="12,1.5 15,8.8 22.8,9.4 16.8,14.4 18.7,22 12,17.9 5.3,22 7.2,14.4 1.2,9.4 9,8.8"/></symbol>
    <symbol id="chev-right" viewBox="0 0 10 16"><polyline points="2,2 8,8 2,14" fill="none" stroke="currentColor" stroke-width="2"/></symbol>
  </defs>
</svg>

<header class="header">
  <div class="brand">
    <div class="brand-name">Hirevale</div>
    <div class="brand-sub">Recruitment</div>
  </div>
  <nav class="nav">
    <a class="active" style="left:531px" href="#">How we work</a>
    <a style="left:650px" href="#">Browse jobs</a>
    <a style="left:759px" href="#">Employers</a>
    <a style="left:857px" href="#">About us</a>
  </nav>
  <a class="btn-login" href="#">Log In</a>
  <a class="btn-register" href="#">Register</a>
</header>

<!-- hero orbit -->
<svg class="orbit" width="1200" height="800" viewBox="0 0 1200 800">
  <circle cx="840" cy="372" r="390" fill="none" stroke="#555" stroke-width="1.3" stroke-dasharray="1.5 6"/>
  <circle cx="837" cy="360" r="227" fill="none" stroke="#777" stroke-width="1.2" stroke-dasharray="1.5 4"/>
  <circle cx="837" cy="358" r="126" fill="var(--soft)"/>
</svg>
<div class="photo" role="img" aria-label="Portrait of a candidate in glasses" style="left:750px;top:271px;width:174px;height:174px;background:radial-gradient(circle at 50% 40%,#9aa5ae,#4c5f70);box-shadow:0 4px 10px rgba(0,0,0,.25)"></div>
<div class="photo" role="img" aria-label="Candidate portrait" style="left:489px;top:104px;width:72px;height:72px;background:linear-gradient(#d9cfc6,#8a8079)"></div>
<div class="photo" role="img" aria-label="Candidate portrait" style="left:707px;top:116px;width:74px;height:74px;background:linear-gradient(#7f8f7a,#262626)"></div>
<div class="photo" role="img" aria-label="Candidate at a laptop" style="left:993px;top:213px;width:72px;height:72px;background:linear-gradient(#e9e2da,#b79a84)"></div>
<div class="photo" role="img" aria-label="Candidate portrait" style="left:580px;top:397px;width:88px;height:88px;background:linear-gradient(#2a2a2a,#6c7a88)"></div>
<div class="photo" role="img" aria-label="Candidate portrait" style="left:914px;top:477px;width:108px;height:108px;background:radial-gradient(circle at 50% 40%,#8a6a5f,#1d1a1a)"></div>
<div class="photo" role="img" aria-label="Candidate portrait" style="left:485px;top:557px;width:54px;height:54px;background:linear-gradient(#a9a9a9,#3b3b3b)"></div>

<h1 class="abs hero-title">We connect top talent with<br>fast growing employers in Asia.</h1>
<p class="abs hero-text">It's the quality of the connection that matters. Our role matching algorithms and talent managers work around.</p>
<a class="btn-red" style="left:48px;top:398px;width:159px;height:49px" href="#">Get Started <svg width="8" height="13" style="color:#fff"><use href="#chev-right"/></svg></a>
<div class="abs scroll-btn"><svg width="16" height="10" viewBox="0 0 16 10"><polyline points="2,2 8,8 14,2" fill="none" stroke="#333" stroke-width="1.5"/></svg></div>

<!-- smart connections -->
<svg class="abs" style="left:150px;top:1095px" width="300" height="120" viewBox="0 0 300 120">
  <path d="M16 10 C 50 70, 110 90, 150 88" fill="none" stroke="#1e8ff0" stroke-width="1.2" stroke-dasharray="1.5 4"/>
  <path d="M182 88 C 225 85, 265 65, 290 45" fill="none" stroke="#1e8ff0" stroke-width="1.2" stroke-dasharray="1.5 4"/>
</svg>
<div class="abs" style="left:300px;top:1170px;width:30px;height:30px;border-radius:50%;background:#fff;box-shadow:0 1px 4px rgba(0,0,0,.18);display:flex;align-items:center;justify-content:center;color:var(--blue-bright)"><svg width="8" height="13"><use href="#chev-right"/></svg></div>

<div class="card p-card" style="left:105px">
  <div class="avatar" role="img" aria-label="Portrait of Marcus Tan" style="background:radial-gradient(circle at 50% 40%,#9aa5ae,#4c5f70)"></div>
  <div class="p-name">Marcus Tan</div>
  <div class="p-role">Senior product designer based in California</div>
  <ul class="p-list">
    <li>User Interface Design</li><li>Prototyping</li><li>Product Design</li><li>3D Design</li><li>Product Development</li>
  </ul>
</div>
<div class="card p-card" style="left:326px;height:352px">
  <div class="avatar" role="img" aria-label="Portrait of Jin Park" style="background:linear-gradient(#7f8f7a,#262626)"></div>
  <div class="p-name">Jin Park</div>
  <div class="p-role">Head of product at Corvix based in Shanghai</div>
  <ul class="p-list">
    <li>Match<span class="tick"></span></li><li>Match<span class="tick"></span></li><li>Match<span class="tick"></span></li><li>Match<span class="tick"></span></li><li>Match<span class="tick"></span></li>
  </ul>
  <div class="match-bar" style="left:0;top:310px;width:204px;height:42px">Profile Match
    <span class="round-ico" style="background:transparent"><svg width="16" height="12" viewBox="0 0 16 12"><polyline points="2,6 6,10 14,2" fill="none" stroke="#fff" stroke-width="1.6"/></svg></span>
  </div>
</div>

<h2 class="section-title" style="left:719px;top:888px">Smart connections</h2>
<p class="section-text" style="left:719px;top:940px;width:325px">It's the quality of the connection that matters. Our role matching algorithms and talent managers work around the clock to find opportunities suitable to your unique profile.</p>

<!-- critical insights -->
<div class="abs insights"></div>
<h2 class="section-title" style="left:92px;top:1434px;color:#fff">Critical insights</h2>
<p class="section-text" style="left:92px;top:1492px;width:380px;color:#fff">Our close interactions with candidates and employers have helped us create a comprehensive database of companies, talents and skills. With HIREVALE, you will gain full access to timely intel to help you make the right career decision.</p>
<a class="btn-outline-white" href="#">Find out more <svg width="8" height="13"><use href="#chev-right"/></svg></a>

<div class="abs insights-photo" role="img" aria-label="Candidate working at a computer in an office"></div>

<div class="card" style="left:901px;top:1349px;width:219px;height:62px;border-radius:3px">
  <div class="photo" role="img" aria-label="Recruiter portrait" style="left:15px;top:8px;width:46px;height:46px;background:linear-gradient(#7f8f7a,#262626)"></div>
  <div class="abs" style="left:75px;top:16px;font-size:11px;line-height:15px;color:var(--ink);font-weight:400">Looking for a senior<br>product designer</div>
</div>
<div class="abs" style="left:901px;top:1428px;width:202px;height:38px;background:var(--red);border-radius:3px;color:#fff;font-size:14px;font-weight:400;display:flex;align-items:center;justify-content:space-between;padding:0 5px 0 18px">Registered users
  <span class="round-ico" style="width:28px;height:28px"><svg width="16" height="16" viewBox="0 0 16 16"><circle cx="8" cy="5" r="3.3" fill="#f3000f"/><path d="M1.5 15c0-4 3-6 6.5-6s6.5 2 6.5 6z" fill="#f3000f"/></svg></span>
</div>
<div class="card" style="left:904px;top:1475px;width:201px;height:235px;border-radius:3px">
  <div class="photo" role="img" aria-label="Portrait of Marcus Tan" style="left:11px;top:12px;width:44px;height:44px;background:radial-gradient(circle at 50% 40%,#9aa5ae,#4c5f70)"></div>
  <div class="abs mini-name" style="left:73px;top:19px">Marcus Tan</div>
  <div class="abs mini-role" style="left:73px;top:37px">Sn Product Designer</div>
  <ul class="mini-list" style="left:17px;right:13px;top:79px">
    <li>User Interface Design<span class="tick"></span></li><li>Prototyping<span class="tick"></span></li><li>Product Design<span class="tick"></span></li><li>3D Design<span class="tick"></span></li><li>Product Development<span class="tick"></span></li>
  </ul>
  <div class="match-bar" style="left:0;top:197px;width:201px;height:38px;font-size:12px;border-radius:0 0 3px 3px">Profile Match
    <span style="display:flex;gap:6px">
      <span class="round-ico" style="width:27px;height:27px"><svg width="14" height="10" viewBox="0 0 14 10"><rect x="1" y="1" width="12" height="8" fill="none" stroke="#1e8ff0" stroke-width="1.3"/><polyline points="1,1 7,6 13,1" fill="none" stroke="#1e8ff0" stroke-width="1.3"/></svg></span>
      <span class="round-ico" style="width:27px;height:27px"><svg width="13" height="13" viewBox="0 0 24 24"><path d="M6.6 10.8c1.4 2.8 3.8 5.1 6.6 6.6l2.2-2.2c.3-.3.7-.4 1-.2 1.1.4 2.3.6 3.6.6.6 0 1 .4 1 1V20c0 .6-.4 1-1 1C10.6 21 3 13.4 3 4c0-.6.4-1 1-1h3.5c.6 0 1 .4 1 1 0 1.3.2 2.5.6 3.6.1.3 0 .7-.2 1z" fill="#1e8ff0"/></svg></span>
    </span>
  </div>
</div>
<div class="card" style="left:1120px;top:1475px;width:80px;height:235px;opacity:.85;overflow:hidden">
  <div class="photo" role="img" aria-label="Candidate portrait" style="left:12px;top:12px;width:44px;height:44px;background:linear-gradient(#6c7a88,#2a2a2a)"></div>
  <ul class="mini-list" style="left:17px;width:120px;top:79px">
    <li>User Interface</li><li>Prototyping</li><li>Product Design</li><li>3D Design</li><li>Product Develop</li>
  </ul>
  <div class="abs" style="left:0;top:197px;width:80px;height:38px;background:var(--blue-bright)"></div>
</div>
<span class="dot" style="left:1089px;top:1727px;background:#fff"></span>
<span class="dot" style="left:1107px;top:1727px"></span>
<span class="dot" style="left:1123px;top:1727px"></span>

<!-- people first -->
<h2 class="section-title" style="left:0;width:1200px;text-align:center;top:1878px">People first</h2>
<p class="section-text" style="left:370px;width:460px;top:1928px;text-align:center">We take the time to really understand you holistically as a person to maximize your potential. As your career counselor, we provide maximum transparency and feedback throughout the process.</p>

<svg class="abs" style="left:340px;top:2425px" width="520" height="115" viewBox="0 0 520 115">
  <path d="M8 5 C 90 85, 170 108, 260 108 C 350 108, 430 85, 512 5" fill="none" stroke="#555" stroke-width="1.2" stroke-dasharray="1.5 5"/>
</svg>

<div class="card t-card" style="left:185px">
  <div class="avatar" role="img" aria-label="Portrait of Mei Lin" style="background:radial-gradient(circle at 50% 40%,#c69a80,#3a2a24)"></div>
  <div class="t-name">Mei Lin</div>
  <div class="t-role">Robotic engineer</div>
  <p class="t-quote">“Hirevale guided me through every part of the process, they used my profile to connect me with some of the top people in my industry. So glad I registered with Hirevale as they kept giving me job updates”</p>
  <div class="stars" style="fill:var(--red)"><svg width="20" height="20"><use href="#star"/></svg><svg width="20" height="20"><use href="#star"/></svg><svg width="20" height="20"><use href="#star"/></svg><svg width="20" height="20"><use href="#star"/></svg><svg width="20" height="20" style="fill:#f78f8f"><use href="#star"/></svg></div>
</div>
<div class="card t-card" style="left:474px">
  <div class="avatar" role="img" aria-label="Portrait of Hao Zhou" style="background:radial-gradient(circle at 50% 40%,#a89a90,#3f3f48)"></div>
  <div class="t-name">Hao Zhou</div>
  <div class="t-role">Senior software engineer</div>
  <p class="t-quote">“Hirevale took my job experience and managed to match me with my dream job. They were helpful every step of the way from interview advice to putting me in contact with leading companies in my field”</p>
  <div class="stars" style="fill:var(--red)"><svg width="20" height="20"><use href="#star"/></svg><svg width="20" height="20"><use href="#star"/></svg><svg width="20" height="20"><use href="#star"/></svg><svg width="20" height="20"><use href="#star"/></svg><svg width="20" height="20"><use href="#star"/></svg></div>
</div>
<div class="card t-card" style="left:764px">
  <div class="avatar" role="img" aria-label="Portrait of Oliver Grant" style="background:radial-gradient(circle at 50% 40%,#c4aa98,#55585c)"></div>
  <div class="t-name">Oliver Grant</div>
  <div class="t-role">Product technologist</div>
  <p class="t-quote">“Setting up my application was extremely easy, their algorithm matched me some top clients instantly. The talent managers also help with the interview process and got me into a fantastic new job”</p>
  <div class="stars" style="fill:var(--red)"><svg width="20" height="20"><use href="#star"/></svg><svg width="20" height="20"><use href="#star"/></svg><svg width="20" height="20"><use href="#star"/></svg><svg width="20" height="20"><use href="#star"/></svg><svg width="20" height="20" style="fill:#f78f8f"><use href="#star"/></svg></div>
</div>
<span class="pager on" style="left:571px;top:2472px"></span>
<span class="pager" style="left:594px;top:2472px"></span>
<span class="pager" style="left:617px;top:2472px"></span>

<!-- footer -->
<footer class="abs footer">
  <div class="f-head" style="left:44px;width:336px">Hirevale</div>
  <div class="f-head" style="left:491px;width:186px">Talents</div>
  <div class="f-head" style="left:721px;width:186px">Employers</div>
  <div class="f-head" style="left:951px;width:186px">About us</div>
  <p class="f-text">HIREVALE is a modern recruitment partner for high potential technology and finance talents. We work closely with hedge funds, systematic trading and FinTech employers experiencing hyper growth in Asia.</p>
  <a class="f-link" style="left:490px;top:114px" href="#">How we work</a>
  <a class="f-link" style="left:490px;top:149px" href="#">Browse jobs</a>
  <a class="f-reg" href="#">Register</a>
  <a class="f-link" style="left:720px;top:114px" href="#">Why HIREVALE</a>
  <a class="f-link" style="left:950px;top:114px" href="#">About HIREVALE</a>
  <a class="f-link" style="left:950px;top:149px" href="#">Working at HIREVALE</a>
  <span class="social" style="left:44px;border-radius:2px" aria-label="Professional network"></span>
  <span class="social" style="left:82px;border-radius:50%" aria-label="Social feed"></span>
  <div class="f-rule"></div>
  <div class="f-small" style="left:44px">Hirevale 2012-2020. All rights reserved.</div>
  <div class="f-small" style="left:973px">Privacy Policy&nbsp; I User Agreement</div>
</footer>

</body>
</html>
```